Maplebrook Self Storage - Business Sign

The sign we are needing designed is our main road sign for our self-storage business. The dimensions of the sign are 57 inches tall x 96 inches wide. We require that our attached logo be on the sign as well as our phone number: 478-216-7745 and website www.MaplebrookStorage.net. Optional information that can be added but not required is our address: 418 Delmont Ridge Pkwy, Ashford Springs, GA 31044.

Industry/Entity Type

Self Storage

Font styles to use
Sans Serif

```html
<!DOCTYPE html>
<html lang="en">
<head>
<meta charset="utf-8">
<title>Maplebrook Self Storage – Road Sign</title>
<link rel="stylesheet" href="https://fonts.googleapis.com/css2?family=Montserrat:wght@400;500;600;700;800&display=swap">
<style>
  :root {
    --sign-white: #f4f5f6;
    --brand-blue: #3b7cc4;
    --charcoal: #464646;
    --logo-grey: #555759;
    --text-white: #ffffff;
  }
  html, body {
    margin: 0;
    padding: 0;
    width: 1200px;
    height: 709px;
    overflow: hidden;
    background: var(--sign-white);
  }
  .sign {
    position: relative;
    width: 1200px;
    height: 709px;
    overflow: hidden;
    background: var(--sign-white);
    font-family: "Montserrat", sans-serif;
  }
  .sign__shapes {
    position: absolute;
    inset: 0;
  }
  .brand {
    position: absolute;
    top: 70px;
    left: 0;
    width: 1200px;
    display: flex;
    justify-content: center;
    align-items: center;
    gap: 22px;
  }
  .brand__mark {
    width: 54px;
    height: 54px;
    background: var(--brand-blue);
  }
  .brand__name {
    font-weight: 700;
    font-size: 58px;
    letter-spacing: 1px;
    color: var(--logo-grey);
  }
  .phone {
    position: absolute;
    left: 40px;
    top: 300px;
    margin: 0;
    font-weight: 800;
    font-size: 142px;
    line-height: 1;
    color: var(--text-white);
    letter-spacing: -1px;
    white-space: nowrap;
  }
  .website {
    position: absolute;
    left: 44px;
    top: 452px;
    margin: 0;
    font-weight: 400;
    font-size: 70px;
    line-height: 1;
    color: var(--text-white);
    white-space: nowrap;
  }
  .address {
    position: absolute;
    left: 270px;
    top: 552px;
    width: 900px;
    height: 58px;
    border-radius: 29px;
    background: var(--charcoal);
    color: var(--text-white);
    font-weight: 500;
    font-size: 27px;
    white-space: nowrap;
    display: flex;
    align-items: center;
    justify-content: flex-end;
    padding-right: 30px;
    box-sizing: border-box;
  }
  .locations-tag {
    position: absolute;
    left: 36px;
    top: 566px;
    width: 270px;
    height: 60px;
    border-radius: 30px;
    background: var(--text-white);
    color: var(--charcoal);
    font-weight: 700;
    font-size: 25px;
    display: flex;
    align-items: center;
    justify-content: center;
  }
</style>
</head>
<body>
  <main class="sign">
    <svg class="sign__shapes" width="1200" height="709" viewBox="0 0 1200 709" aria-hidden="true">
      <polygon class="accent-stripe-top" points="0,292 720,236 0,326" fill="#464646"/>
      <polygon class="blue-band" points="0,336 1200,176 1200,580 0,709" fill="#3b7cc4"/>
      <polygon class="accent-stripe-bottom" points="560,660 1200,586 1200,612" fill="#464646"/>
    </svg>

    <header class="brand">
      <span class="brand__mark"></span>
      <span class="brand__name">Maplebrook Self Storage</span>
    </header>

    <p class="phone">478-216-7745</p>
    <p class="website">www.MaplebrookStorage.net</p>

    <div class="address">418 Delmont Ridge Pkwy, Ashford Springs, GA 31044</div>
    <div class="locations-tag">OUR LOCATIONS</div>
  </main>
</body>
</html>
```